Design some Business Cards for Valdor Capital Group

Looking for the most Luxury, Best, Unique business cards. We are looking for raised uv gloss and foil business cards (which ever one we like more) for company called Valdor Capital Group. Please see the website for details.

```html
<!DOCTYPE html>
<html lang="en">
<head>
<meta charset="utf-8">
<title>Valdor Capital Group – Business Cards</title>
<link rel="stylesheet" href="https://fonts.googleapis.com/css2?family=Montserrat:wght@300;400;600&display=swap">
<style>
  :root {
    --stage: #3b3b3d;
    --stage-dark: #262628;
    --card-dark: #252526;
    --white: #ffffff;
    --soft-white: #e6e6e6;
    --accent: #c8242b;
    --sky-top: #6c7ea6;
    --sky-mid: #a795ad;
    --sky-glow: #e8b7a4;
    --water: #8f7f8c;
  }
  * { box-sizing: border-box; margin: 0; padding: 0; }
  html, body { width: 1200px; height: 900px; overflow: hidden; }
  body {
    background: radial-gradient(ellipse at 50% 45%, var(--stage) 0%, var(--stage-dark) 100%);
    font-family: "Montserrat", sans-serif;
    color: var(--white);
    position: relative;
  }
  .card {
    position: absolute;
    width: 560px;
    height: 320px;
    overflow: hidden;
    box-shadow: 0 14px 30px rgba(0,0,0,0.45);
  }
  .card--front { left: 90px; top: 110px; }
  .card--back { left: 550px; top: 470px; background: var(--card-dark); }

  .skyline-photo {
    position: absolute; inset: 0;
    background: linear-gradient(180deg, var(--sky-top) 0%, var(--sky-mid) 40%, var(--sky-glow) 62%, #5a5566 70%, var(--water) 100%);
  }
  .card--front .skyline-photo::after {
    content: ""; position: absolute; inset: 0; background: rgba(20,20,30,0.18);
  }

  .brand-name {
    font-weight: 400;
    text-transform: uppercase;
    color: var(--white);
    line-height: 1.05;
  }
  .front-brand {
    position: absolute; left: 250px; top: 168px; z-index: 2;
  }
  .front-brand .brand-name { font-size: 27px; letter-spacing: 1px; }
  .front-brand .brand-name span { display: block; font-size: 12px; letter-spacing: 2.6px; }
  .front-tagline {
    position: absolute; left: 170px; top: 248px; z-index: 2;
    font-size: 10px; letter-spacing: 1.6px; font-weight: 400;
  }

  .back-photo { position: absolute; inset: 0; }
  .back-info {
    position: absolute; right: 40px; top: 36px; text-align: right;
  }
  .back-info .brand-name { font-size: 29px; letter-spacing: 1px; }
  .back-info .brand-name span { display: block; font-size: 12px; letter-spacing: 2.8px; }
  .person-name { margin-top: 14px; font-size: 17px; font-weight: 600; }
  .person-role { font-size: 10px; letter-spacing: 1px; font-weight: 300; }
  .accent-rule {
    position: absolute; right: 60px; top: 150px; width: 190px; height: 2px;
    background: linear-gradient(90deg, transparent, var(--accent));
  }
  .contact-list {
    position: absolute; right: 28px; top: 170px; list-style: none;
    font-size: 10px; font-weight: 300; letter-spacing: 1.2px; color: var(--soft-white);
    text-align: right;
  }
  .contact-list li { display: flex; justify-content: flex-end; align-items: center; gap: 12px; height: 20px; }
  .contact-icon { width: 12px; height: 12px; flex: none; }
  .contact-icon--blank { visibility: hidden; }
</style>
</head>
<body>

<section class="card card--front" aria-label="Business card front">
  <div class="skyline-photo" role="img" aria-label="Photograph of a city skyline with a tall tower across the water at dusk"></div>
  <div class="front-brand">
    <p class="brand-name">Valdor <span>Capital Group</span></p>
  </div>
  <p class="front-tagline">INVEST | BUILD | COMMERCIAL | RESIDENTIAL</p>
</section>

<section class="card card--back" aria-label="Business card back">
  <svg class="back-photo" width="560" height="320" viewBox="0 0 560 320">
    <defs>
      <linearGradient id="photoTone" x1="0" y1="0" x2="0" y2="1">
        <stop offset="0" stop-color="#6c7ea6"/>
        <stop offset="0.45" stop-color="#a795ad"/>
        <stop offset="0.62" stop-color="#e8b7a4"/>
        <stop offset="0.72" stop-color="#5a5566"/>
        <stop offset="1" stop-color="#8f7f8c"/>
      </linearGradient>
    </defs>
    <path d="M0 130 Q150 125 230 180 Q255 250 250 320 L0 320 Z" fill="url(#photoTone)" role="img" aria-label="Photograph of a city skyline with a tall tower reflected in the water"/>
  </svg>

  <div class="back-info">
    <p class="brand-name">Valdor <span>Capital Group</span></p>
    <p class="person-name">Marek Dolinski</p>
    <p class="person-role">CEO</p>
  </div>
  <div class="accent-rule"></div>

  <ul class="contact-list">
    <li>O: 555 210 4417
      <svg class="contact-icon" viewBox="0 0 12 12"><path d="M3 1 L5 3.5 L4 4.8 Q5 7 7.2 8 L8.5 7 L11 9 L10 11 Q5 11 1 6 Q1 3 3 1 Z" fill="none" stroke="#e6e6e6" stroke-width="0.9"/></svg></li>
    <li>C: 555 388 0192 <svg class="contact-icon contact-icon--blank" viewBox="0 0 12 12"></svg></li>
    <li>www.valdorcapitalgroup.com
      <svg class="contact-icon" viewBox="0 0 12 12"><circle cx="6" cy="6" r="5" fill="none" stroke="#e6e6e6" stroke-width="0.9"/><ellipse cx="6" cy="6" rx="2.2" ry="5" fill="none" stroke="#e6e6e6" stroke-width="0.8"/><line x1="1" y1="6" x2="11" y2="6" stroke="#e6e6e6" stroke-width="0.8"/></svg></li>
    <li>marek@valdorcapitalgroup.com
      <svg class="contact-icon" viewBox="0 0 12 12"><rect x="1" y="2.5" width="10" height="7" fill="none" stroke="#e6e6e6" stroke-width="0.9"/><path d="M1 2.5 L6 6.5 L11 2.5" fill="none" stroke="#e6e6e6" stroke-width="0.9"/></svg></li>
    <li>lic#20417735 | mol lic#18264 <svg class="contact-icon contact-icon--blank" viewBox="0 0 12 12"></svg></li>
  </ul>
</section>

</body>
</html>
```